TRENDY & MODERN BUSINESS CARD DESIGN for Media Company *

I need a minimalistic - clean - modern and professional business card layout and design for MEDIA & PHOTOGRAPHY STUDIO.

We do NOT have a logo, and not really looking for one - but rather excellent typography and design. We would consider the 3 as a focal point.

We do personal and commercial photography.

Target Market(s)

Personal and commercial photography clientele

Contact Information for Business Card

KYT size - from kyt.com / size guidelines are enclosed in the brief

Font styles to use
Sans Serif

Colors
f78f20
eda3c7
cee9f5
0555a3
e667a6
fbf289

Requirements
Must have
• Clean lines - Modern layout
Nice to have
• All blue background as an option - use color palette in brief please.
Should not have
• Old fashion fonts and regular fonts.

```html
<!DOCTYPE html>
<html lang="en">
<head>
<meta charset="utf-8">
<title>Halden Lens Media — Business Cards</title>
<link href="https://fonts.googleapis.com/css2?family=Work+Sans:wght@300;400;500&display=swap" rel="stylesheet">
<style>
  :root {
    --backdrop: #141414;
    --card: #1d1d1d;
    --card-edge: #262626;
    --emboss: #3a3a3a;
    --emboss-soft: #363636;
    --rule: #3e3e3e;
    --print: #d6d6d6;
    --print-bright: #ececec;
  }
  * { margin: 0; padding: 0; box-sizing: border-box; }
  html, body {
    width: 1200px;
    height: 900px;
    overflow: hidden;
    background: var(--backdrop);
    font-family: "Work Sans", sans-serif;
  }
  .canvas {
    position: relative;
    width: 1200px;
    height: 900px;
  }
  .card {
    position: absolute;
    left: 250px;
    width: 700px;
    height: 400px;
    background: linear-gradient(160deg, var(--card-edge) 0%, var(--card) 55%, #1a1a1a 100%);
    overflow: hidden;
  }
  .card--back { top: 25px; }
  .card--front { top: 475px; }

  /* portrait face, turned so lines read bottom to top */
  .face {
    position: absolute;
    left: 150px;
    top: -150px;
    width: 400px;
    height: 700px;
    transform: rotate(-90deg);
  }

  .wordmark { position: absolute; left: 34px; }
  .card--front .wordmark { top: 46px; }
  .card--back .wordmark { top: 376px; }

  .wordmark__name {
    font-size: 26px;
    font-weight: 500;
    letter-spacing: 2px;
    color: var(--emboss);
    line-height: 1.1;
    white-space: nowrap;
  }
  .wordmark__rule {
    width: 210px;
    height: 1px;
    background: var(--rule);
    margin: 8px 0 6px;
  }
  .wordmark__tagline {
    font-size: 15px;
    font-weight: 400;
    letter-spacing: 1.5px;
    word-spacing: 4px;
    color: var(--emboss);
    white-space: nowrap;
  }

  .person { position: absolute; left: 34px; top: 196px; }
  .person__name {
    font-size: 23px;
    font-weight: 400;
    letter-spacing: 2px;
    color: var(--emboss-soft);
    line-height: 1.1;
  }
  .person__title {
    font-size: 17px;
    font-weight: 400;
    letter-spacing: 1.5px;
    color: var(--emboss-soft);
  }

  .details {
    position: absolute;
    left: 34px;
    font-size: 18px;
    font-weight: 300;
    font-style: normal;
    letter-spacing: 2px;
    line-height: 1.55;
    white-space: nowrap;
  }
  .details--address { top: 336px; color: var(--print); }
  .details--contact { top: 452px; color: var(--print); }
  .details--locations { top: 568px; color: var(--print-bright); font-weight: 400; }
</style>
</head>
<body>
  <main class="canvas">
    <section class="card card--back" aria-label="Card back">
      <div class="face">
        <div class="wordmark">
          <p class="wordmark__name">HALDEN LENS MEDIA</p>
          <div class="wordmark__rule"></div>
          <p class="wordmark__tagline">Seeing Light. Keeping Moments.</p>
        </div>
      </div>
    </section>

    <section class="card card--front" aria-label="Card front">
      <div class="face">
        <div class="wordmark">
          <p class="wordmark__name">HALDEN LENS MEDIA</p>
          <div class="wordmark__rule"></div>
          <p class="wordmark__tagline">Seeing Light. Keeping Moments.</p>
        </div>
        <div class="person">
          <p class="person__name">MARISOL VEGA</p>
          <p class="person__title">Founder &amp;Media Director</p>
        </div>
        <address class="details details--address">
          2400 Coral Way<br>9th Floor Miami, FL 33145
        </address>
        <p class="details details--contact">
          (305) 555-0148<br>mara@haldenlens.com
        </p>
        <p class="details details--locations">
          Studios: Tampa • Boston •<br>Denver • Tulum • Milano
        </p>
      </div>
    </section>
  </main>
</body>
</html>
```